Awesome design needed for standup comedy portal

We need a website designed for a new portal (grinvault.net) dedicated to standup comedy.

- homepage
- featured "hero" content at top
- banner advertising
- browse comics
- browse venues
- search
- signup / login
- social media links

- comic page
- name
- pictures
- calendar of performances
- list of albums (with buy buttons)
- list of specials (Streamora, Tunebox, etc. with buy buttons)
- reviews
- latest tweets
- latests picshelf photos
- links to social media accounts
- links to flmx, podcast

- venue page
- name
- pictures
- address, phone number
- calendar of events
- reviews
- latest tweets
- links to flmx, podcast

Target Market(s)

Fans of standup comedy and comedians

Number of Pages Required

3 page

Font styles to use
Sans Serif

Requirements
Must have
• Will eventually be implemented in bootstrap, so please keep that in mind

```html
<!DOCTYPE html>
<html lang="en">
<head>
<meta charset="utf-8">
<title>Grinvault – Comic page</title>
<link href="https://fonts.googleapis.com/css2?family=Roboto:wght@300;400;500;700&family=Roboto+Condensed:wght@400;700&display=swap" rel="stylesheet">
<style>
:root{
  --sky:#a9c6dc;
  --page:#ffffff;
  --purple:#8e3f91;
  --pink:#d4458c;
  --lavender:#d9cde6;
  --lavender-deep:#c4b3dc;
  --panel:#ebe3ef;
  --panel-light:#f6eff4;
  --text:#4a4550;
  --muted:#6b6470;
  --footer:#666666;
  --white:#ffffff;
}
*{box-sizing:border-box;margin:0;padding:0}
html,body{width:870px;height:1200px;overflow:hidden}
body{background:var(--sky);font-family:"Roboto",Arial,sans-serif;color:var(--text);position:relative}
.page{position:absolute;left:86px;top:46px;width:704px;height:1100px;background:var(--page)}
.abs{position:absolute}

/* header */
.site-header{left:0;top:0;width:704px;height:124px;background:linear-gradient(90deg,#b8404f 0%,#b0663e 22%,#8b7a5a 42%,#6d6f8e 58%,#3f8d7c 78%,#2fae8e 100%);border-bottom:3px solid #d7d0d8}
.brand{left:44px;top:8px;width:110px;height:104px;display:flex;align-items:flex-end;justify-content:center}
.brand-mark{left:18px;top:0;width:74px;height:74px;border-radius:50%;background:radial-gradient(circle at 50% 45%,#e0453a,#b3201f)}
.brand-name{position:relative;font-family:"Roboto Condensed",Arial,sans-serif;font-weight:700;font-size:23px;color:var(--white);letter-spacing:.5px}
.header-mic{left:585px;top:36px;width:60px;height:86px;border-radius:30px 30px 8px 8px;background:linear-gradient(180deg,rgba(200,240,235,.55),rgba(120,190,180,.25))}
.nav{left:167px;top:93px;display:flex;gap:2px}
.nav a,.auth a{display:block;height:20px;line-height:20px;font-size:12.5px;color:var(--white);text-decoration:none;text-align:center;letter-spacing:.5px;background:linear-gradient(90deg,rgba(142,63,145,.75),rgba(142,63,145,.45))}
.nav a.active{background:rgba(170,90,220,.85)}
.nav .w1{width:77px}.nav .w2{width:66px}.nav .w3{width:90px}.nav .w4{width:86px}
.auth{left:527px;top:93px;display:flex;gap:2px}
.auth a{width:73px;background:var(--purple)}
.social-top{left:544px;top:6px;display:flex;gap:6px;align-items:center}
.dot{width:20px;height:20px;border-radius:50%;background:var(--pink)}
.cart{width:21px;height:21px;background:var(--purple);margin-left:4px}

/* search */
.search{left:167px;top:132px;width:428px;height:22px;border:1px solid #bbb;background:var(--white)}
.search-btn{right:-1px;top:-1px;width:22px;height:22px;background:var(--purple)}

/* calendar */
.calendar{left:23px;top:160px;width:165px;height:186px;background:var(--panel);box-shadow:0 1px 2px rgba(0,0,0,.2)}
.panel-head{height:18px;line-height:18px;text-align:center;font-size:10px;color:var(--pink);background:var(--lavender-deep);letter-spacing:.5px}
.cal-grid{display:grid;grid-template-columns:repeat(7,1fr);padding:4px 6px 0}
.cal-grid span{height:24.5px;line-height:24.5px;text-align:center;font-size:7.6px;color:#333;font-weight:500}
.cal-grid .dow{height:18px;line-height:18px;font-size:6.8px;color:#555}
.cal-grid .on{position:relative;color:var(--white)}
.cal-grid .on::before{content:"";position:absolute;left:50%;top:50%;width:13px;height:13px;margin:-6.5px 0 0 -6.5px;border-radius:50%;background:var(--pink)}
.cal-grid .on b{position:relative;font-weight:500}
.legend{padding:3px 16px;font-size:9.5px;display:flex;align-items:center;gap:6px;color:#333}
.legend i{width:7px;height:7px;border-radius:50%;background:var(--pink)}

/* hero slider */
.hero{left:196px;top:160px;width:290px;height:189px;background:radial-gradient(circle at 50% 55%,#bfe6ff 0%,#5aa6e6 45%,#2c6fc1 100%);box-shadow:0 1px 3px rgba(0,0,0,.25)}
.hero-title{left:0;top:0;width:290px;height:27px;line-height:27px;padding-left:8px;font-size:11.5px;color:var(--white);background:rgba(200,190,240,.5);letter-spacing:.4px}
.hero svg{position:absolute}
.links{left:291px;top:361px;display:flex;gap:7px;align-items:center}
.pill{width:54px;height:17px;background:var(--purple);color:var(--white);font-family:"Roboto Condensed",Arial,sans-serif;font-weight:700;font-size:10px;line-height:17px;text-align:center}
.cdot{width:20px;height:20px;border-radius:50%;background:var(--purple)}

/* copy */
.copy{left:29px;top:397px;width:452px;font-size:7.9px;line-height:10.3px;color:var(--muted);text-transform:uppercase;font-weight:400}
.copy p+p{margin-top:10px}
.book{left:395px;top:558px;width:86px;height:22px;line-height:22px;text-align:center;background:var(--purple);color:var(--white);font-size:11.5px;letter-spacing:.4px}

/* sidebar */
.sidebar{left:496px;top:160px;width:180px;height:594px;background:var(--panel);overflow:hidden}
.side-head{height:26px;line-height:26px;text-align:center;font-size:10px;color:var(--pink);background:var(--panel-light);font-weight:500}
.tweet{display:flex;gap:5px;padding:4px 5px 0;height:49px}
.thumb{width:40px;height:41px;flex:none;background:linear-gradient(160deg,#5e6a60,#9a9a8a 60%,#3a3f3a)}
.tweet h4{font-size:8.4px;color:var(--pink);font-weight:700}
.tweet p{font-size:6.6px;line-height:8px;color:var(--muted)}
.icons{display:flex;gap:5px;margin-top:2px}
.icons svg{width:8px;height:8px}
.side-head.insta{margin-top:6px}
.post{padding:9px 5px 0;height:112px}
.post h4{font-size:8.4px;color:var(--pink);font-weight:700;display:flex;align-items:center;gap:4px}
.post h4 i{width:8px;height:8px;border-radius:50%;background:#333}
.post .photo{height:49px;margin-top:2px;background:linear-gradient(90deg,#c85a3a,#e0855a 60%,#d6a070)}
.post p{font-size:6.6px;line-height:8px;color:var(--muted);margin-top:3px;padding-right:40px}

/* albums and specials */
.shelf{top:593px;width:222px;height:186px;background:var(--panel)}
.shelf .panel-head{height:26px;line-height:26px;font-size:11.5px;color:var(--white);background:var(--lavender)}
.item{display:flex;align-items:center;gap:5px;padding:5px 5px 0;height:51px}
.cover{width:40px;height:40px;flex:none}
.item .txt{flex:1}
.item h4{font-size:8.4px;color:var(--pink);font-weight:700}
.item p{font-size:6.3px;line-height:7.6px;color:var(--muted);text-transform:uppercase}
.buy{width:48px;height:22px;line-height:22px;text-align:center;background:var(--purple);color:var(--white);font-size:11.5px;flex:none;margin-right:2px}
.tunebox{border-radius:50%;background:var(--white);border:1px solid #ccc;display:flex;align-items:center;justify-content:center;font-size:7px;color:var(--pink);font-weight:500}
.streamora{background:#111;display:flex;align-items:center;justify-content:center;font-size:6.5px;color:var(--white);font-weight:500}

/* reviews */
.review{top:788px;width:320px;height:73px;background:var(--panel-light);border:1px solid #d8d0d8;box-shadow:0 1px 2px rgba(0,0,0,.15);padding:4px 6px}
.review h4{font-size:10px;font-weight:500;color:var(--pink);display:flex;align-items:center;gap:4px;letter-spacing:.3px}
.review h4 .date{color:#9a8ea0;font-weight:400}
.stars{display:flex;gap:2px}
.stars svg{width:12px;height:12px}
.review p{font-size:7.8px;line-height:15.5px;color:#444;margin-top:3px;text-transform:uppercase;font-weight:400}

/* footer */
.site-footer{left:0;top:1003px;width:704px;height:97px;background:var(--footer);color:var(--white)}
.contact{left:54px;top:15px;display:grid;grid-template-columns:38px auto;align-items:baseline;row-gap:3px;font-size:10.5px;line-height:15.5px}
.contact dt{font-size:6.5px;letter-spacing:.3px}
.foot-brand{left:320px;top:12px;width:70px;text-align:center}
.foot-brand .mark{width:30px;height:30px;border-radius:50%;background:#c32a25;margin:0 auto}
.foot-brand span{font-family:"Roboto Condensed",Arial,sans-serif;font-weight:700;font-size:11px;color:var(--white)}
.copyright{left:0;top:80px;width:704px;text-align:center;font-size:7.5px;letter-spacing:.3px}
.foot-social{left:448px;top:23px;display:flex;gap:12px}
.foot-social a{width:39px;height:39px;border-radius:50%;background:var(--pink);color:var(--white);font-size:6.2px;text-decoration:none;display:flex;align-items:center;justify-content:center;box-shadow:0 1px 3px rgba(0,0,0,.3)}
</style>
</head>
<body>
<main class="page">

  <header class="site-header abs">
    <div class="brand abs">
      <div class="brand-mark abs" role="img" aria-label="Grinvault mascot emblem"></div>
      <span class="brand-name">GRINVAULT</span>
    </div>
    <div class="header-mic abs" role="img" aria-label="Vintage microphone photo"></div>
    <nav class="nav abs">
      <a class="w1" href="#">HOME</a>
      <a class="w2 active" href="#">COMIC</a>
      <a class="w3" href="#">VENUE</a>
      <a class="w4" href="#">CONTACT</a>
    </nav>
    <div class="auth abs"><a href="#">LOGIN</a><a href="#">SIGNUP</a></div>
    <div class="social-top abs" aria-label="Social links">
      <span class="dot" title="Picshelf"></span><span class="dot" title="Chirpline"></span><span class="dot" title="Friendwall"></span><span class="dot" title="Pinvale"></span>
      <span class="cart" title="Cart"></span>
    </div>
  </header>

  <form class="search abs">
    <div class="search-btn abs">
      <svg width="22" height="22" viewBox="0 0 22 22"><circle cx="10" cy="10" r="5" fill="none" stroke="#fff" stroke-width="2"/><line x1="13.5" y1="13.5" x2="17" y2="17" stroke="#fff" stroke-width="2.2"/></svg>
    </div>
  </form>

  <section class="calendar abs">
    <div class="panel-head">MARCH</div>
    <div class="cal-grid">
      <span class="dow">MON</span><span class="dow">TUE</span><span class="dow">WED</span><span class="dow">THU</span><span class="dow">FRI</span><span class="dow">SAT</span><span class="dow">SUN</span>
      <span></span><span></span><span>1</span><span>2</span><span>3</span><span>4</span><span class="on"><b>5</b></span>
      <span>6</span><span>7</span><span class="on"><b>8</b></span><span>9</span><span>10</span><span>11</span><span>12</span>
      <span>13</span><span class="on"><b>14</b></span><span>15</span><span>16</span><span>17</span><span class="on"><b>18</b></span><span>19</span>
      <span>20</span><span>21</span><span>22</span><span>23</span><span>24</span><span>25</span><span>26</span>
      <span class="on"><b>27</b></span><span>28</span><span>29</span><span class="on"><b>30</b></span><span></span><span></span><span></span>
    </div>
    <div class="legend"><i></i>AVALIABLE DATES</div>
  </section>

  <section class="hero abs" role="img" aria-label="Featured photo of a studio microphone">
    <div class="hero-title abs">MAURIS PORTTITOR</div>
    <svg style="left:10px;top:85px" width="12" height="40" viewBox="0 0 12 40"><polyline points="10,2 3,20 10,38" fill="none" stroke="rgba(255,255,255,.7)" stroke-width="2"/></svg>
    <svg style="left:268px;top:85px" width="12" height="40" viewBox="0 0 12 40"><polyline points="2,2 9,20 2,38" fill="none" stroke="rgba(255,255,255,.7)" stroke-width="2"/></svg>
  </section>

  <div class="links abs">
    <span class="pill">flmx</span>
    <span class="cdot" title="Podcast"></span><span class="cdot" title="Pinvale"></span><span class="cdot" title="Chirpline"></span><span class="cdot" title="Picshelf"></span><span class="cdot" title="Friendwall"></span>
  </div>

  <article class="copy abs">
    <p>Lorem ipsum dolor sit amet, consectetur adipiscing elit. Pellentesque a magna et odio fringilla varius. Quisque ut luctus nisi. Praesent suscipit aliquam convallis. Nam at mauris fermentum, aliquet elit sed, pellentesque magna. Fusce quis vulputate orci. Vivamus sed auctor metus. Cras auctor eros quis ex auctor tristique. Pellentesque porta mi sit amet eros ullamcorper, id scelerisque libero semper. Sed ac magna ex. Fusce iaculis feugiat nisi non vulputate. Fusce congue sit amet quam at lacinia. Duis ac molestie ex, ac accumsan purus. Quisque finibus quis mi ac eleifend. Pellentesque convallis nisi in ex gravida hendrerit. Curabitur condimentum nulla quis dignissim finibus.</p>
    <p>Nullam laoreet rutrum facilisis. Nunc ac auctor nisi. Vestibulum diam nisi, condimentum sed facilisis consequat, lacinia vel sapien. Aenean tristique enim a orci molestie, eget dapibus augue congue. Maecenas mauris dui, pharetra nec bibendum quis, aliquam vel dolor. Pellentesque pulvinar quam et leo accumsan, sit amet semper eros pellentesque. Nullam eget pharetra enim, luctus luctus nibh. Nullam posuere tempus congue. Morbi finibus non massa quis tristique. Integer ut tincidunt dolor.</p>
  </article>
  <a class="book abs">BOOK NOW</a>

  <aside class="sidebar abs">
    <div class="side-head">CHIRPLINE</div>
    <div class="tweet"><div class="thumb" role="img" aria-label="Tweet photo"></div><div><h4>MAECENAS</h4><p>PHASELLUS NEC ANTE VITAE ANTE MATTIS TEMPUS EGET NEC EST.</p><div class="icons"><svg viewBox="0 0 8 8"><path d="M1 4a3 3 0 0 1 5-2M7 4a3 3 0 0 1-5 2" fill="none" stroke="#444"/></svg><svg viewBox="0 0 8 8"><path d="M1 7 Q2 3 6 3 L4 1 M6 3 L4 5" fill="none" stroke="#444"/></svg><svg viewBox="0 0 8 8"><rect x="0.5" y="1.5" width="7" height="5" fill="#444"/></svg></div></div></div>
    <div class="tweet"><div class="thumb" role="img" aria-label="Tweet photo"></div><div><h4>MAECENAS</h4><p>PHASELLUS NEC ANTE VITAE ANTE MATTIS TEMPUS EGET NEC EST.</p><div class="icons"><svg viewBox="0 0 8 8"><path d="M1 4a3 3 0 0 1 5-2M7 4a3 3 0 0 1-5 2" fill="none" stroke="#444"/></svg><svg viewBox="0 0 8 8"><path d="M1 7 Q2 3 6 3 L4 1 M6 3 L4 5" fill="none" stroke="#444"/></svg><svg viewBox="0 0 8 8"><rect x="0.5" y="1.5" width="7" height="5" fill="#444"/></svg></div></div></div>
    <div class="tweet"><div class="thumb" role="img" aria-label="Tweet photo"></div><div><h4>MAECENAS</h4><p>PHASELLUS NEC ANTE VITAE ANTE MATTIS TEMPUS EGET NEC EST.</p><div class="icons"><svg viewBox="0 0 8 8"><path d="M1 4a3 3 0 0 1 5-2M7 4a3 3 0 0 1-5 2" fill="none" stroke="#444"/></svg><svg viewBox="0 0 8 8"><path d="M1 7 Q2 3 6 3 L4 1 M6 3 L4 5" fill="none" stroke="#444"/></svg><svg viewBox="0 0 8 8"><rect x="0.5" y="1.5" width="7" height="5" fill="#444"/></svg></div></div></div>
    <div class="tweet"><div class="thumb" role="img" aria-label="Tweet photo"></div><div><h4>MAECENAS</h4><p>PHASELLUS NEC ANTE VITAE ANTE MATTIS TEMPUS EGET NEC EST.</p><div class="icons"><svg viewBox="0 0 8 8"><path d="M1 4a3 3 0 0 1 5-2M7 4a3 3 0 0 1-5 2" fill="none" stroke="#444"/></svg><svg viewBox="0 0 8 8"><path d="M1 7 Q2 3 6 3 L4 1 M6 3 L4 5" fill="none" stroke="#444"/></svg><svg viewBox="0 0 8 8"><rect x="0.5" y="1.5" width="7" height="5" fill="#444"/></svg></div></div></div>
    <div class="side-head insta">PICSHELF</div>
    <div class="post"><h4><i></i>JOHN</h4><div class="photo" role="img" aria-label="Photo of a golden microphone on orange backdrop"></div><p>PHASELLUS NEC ANTE VITAE ANTE MATTIS TEMPUS EGET NEC EST.</p><div class="icons"><svg viewBox="0 0 8 8"><path d="M4 7 L1 4 A1.6 1.6 0 0 1 4 2 A1.6 1.6 0 0 1 7 4 Z" fill="#444"/></svg><svg viewBox="0 0 8 8"><path d="M1 4a3 3 0 0 1 5-2M7 4a3 3 0 0 1-5 2" fill="none" stroke="#444"/></svg><svg viewBox="0 0 8 8"><path d="M1 7 Q2 3 6 3 L4 1 M6 3 L4 5" fill="none" stroke="#444"/></svg><svg viewBox="0 0 8 8"><rect x="0.5" y="1.5" width="7" height="5" fill="#444"/></svg></div></div>
    <div class="post"><h4><i></i>JOHN</h4><div class="photo" role="img" aria-label="Photo of a golden microphone on orange backdrop"></div><p>PHASELLUS NEC ANTE VITAE ANTE MATTIS TEMPUS EGET NEC EST.</p><div class="icons"><svg viewBox="0 0 8 8"><path d="M4 7 L1 4 A1.6 1.6 0 0 1 4 2 A1.6 1.6 0 0 1 7 4 Z" fill="#444"/></svg><svg viewBox="0 0 8 8"><path d="M1 4a3 3 0 0 1 5-2M7 4a3 3 0 0 1-5 2" fill="none" stroke="#444"/></svg><svg viewBox="0 0 8 8"><path d="M1 7 Q2 3 6 3 L4 1 M6 3 L4 5" fill="none" stroke="#444"/></svg><svg viewBox="0 0 8 8"><rect x="0.5" y="1.5" width="7" height="5" fill="#444"/></svg></div></div>
    <div class="post"><h4><i></i>JOHN</h4><div class="photo" role="img" aria-label="Photo of a golden microphone on orange backdrop"></div><p>PHASELLUS NEC ANTE VITAE ANTE MATTIS TEMPUS EGET NEC EST.</p><div class="icons"><svg viewBox="0 0 8 8"><path d="M4 7 L1 4 A1.6 1.6 0 0 1 4 2 A1.6 1.6 0 0 1 7 4 Z" fill="#444"/></svg><svg viewBox="0 0 8 8"><path d="M1 4a3 3 0 0 1 5-2M7 4a3 3 0 0 1-5 2" fill="none" stroke="#444"/></svg><svg viewBox="0 0 8 8"><path d="M1 7 Q2 3 6 3 L4 1 M6 3 L4 5" fill="none" stroke="#444"/></svg><svg viewBox="0 0 8 8"><rect x="0.5" y="1.5" width="7" height="5" fill="#444"/></svg></div></div>
  </aside>

  <section class="shelf abs" style="left:21px">
    <div class="panel-head">ALBUMS</div>
    <div class="item"><div class="cover" style="background:linear-gradient(135deg,#3fb3d8,#1b7fb0)" role="img" aria-label="Album cover art"></div><div class="txt"><h4>ALIQUAM</h4><p>Ut nec libero sed orci fringilla molestie. Sed gravida lacus vel finibus tincidunt. Maecenas vitae elementum dui aliquam</p></div><a class="buy">BUY</a></div>
    <div class="item"><div class="cover" style="background:linear-gradient(135deg,#4a3a3a,#1f1a1c)" role="img" aria-label="Album cover art"></div><div class="txt"><h4>DONEC</h4><p>Duis ullamcorper erat turpis, vitae pretium diam eleifend vel. Donec rutrum purus sed iaculis eu augue vitae faucibus quisque</p></div><a class="buy">BUY</a></div>
    <div class="item"><div class="cover" style="background:linear-gradient(135deg,#3a5a8a,#1c2840)" role="img" aria-label="Album cover art"></div><div class="txt"><h4>ETIAM</h4><p>Proin suscipit dui non tincidunt tempor. Vestibulum scelerisque, dolor at porttitor tempus, eros tortor aliquam purus.</p></div><a class="buy">BUY</a></div>
  </section>

  <section class="shelf abs" style="left:264px">
    <div class="panel-head">SPECIALS</div>
    <div class="item"><div class="cover tunebox">Tunebox</div><div class="txt"><h4>PHASELLUS</h4><p>Fusce rutrum lectus tellus, ac tristique orci cursus id. Integer in volutpat nulla. Nam molestie pretium felis quis varius.</p></div><a class="buy">BUY</a></div>
    <div class="item"><div class="cover tunebox">Tunebox</div><div class="txt"><h4>SOLLICITUDIN</h4><p>Nunc auctor velit enim, nec fringilla nulla tincidunt non. Vivamus tincidunt, ex id molestie, nisl nunc finibus</p></div><a class="buy">BUY</a></div>
    <div class="item"><div class="cover streamora">Streamora</div><div class="txt"><h4>MORBI</h4><p>Donec auctor condimentum mauris, at fringilla libero vestibulum at. Aliquam erat volutpat.</p></div><a class="buy">BUY</a></div>
  </section>

  <section class="review abs" style="left:21px">
    <h4><span class="stars">
      <svg viewBox="0 0 12 12"><polygon points="6,0.5 7.6,4.3 11.6,4.5 8.5,7 9.5,11 6,8.8 2.5,11 3.5,7 0.4,4.5 4.4,4.3" fill="#d4458c"/></svg>
      <svg viewBox="0 0 12 12"><polygon points="6,0.5 7.6,4.3 11.6,4.5 8.5,7 9.5,11 6,8.8 2.5,11 3.5,7 0.4,4.5 4.4,4.3" fill="#d4458c"/></svg>
      <svg viewBox="0 0 12 12"><polygon points="6,0.5 7.6,4.3 11.6,4.5 8.5,7 9.5,11 6,8.8 2.5,11 3.5,7 0.4,4.5 4.4,4.3" fill="#e9a9c8"/></svg>
      <svg viewBox="0 0 12 12"><polygon points="6,0.5 7.6,4.3 11.6,4.5 8.5,7 9.5,11 6,8.8 2.5,11 3.5,7 0.4,4.5 4.4,4.3" fill="#e9a9c8"/></svg>
      <svg viewBox="0 0 12 12"><polygon points="6,0.5 7.6,4.3 11.6,4.5 8.5,7 9.5,11 6,8.8 2.5,11 3.5,7 0.4,4.5 4.4,4.3" fill="#e9a9c8"/></svg>
    </span>&nbsp;PRAESENT <span class="date">&nbsp;| 10 MARCH 2017</span></h4>
    <p>Donec vitae laoreet justo, et euismod justo. Vestibulum sit amet faucibus justo. Pellentesque maximus ex sed hendrerit sodales. Aliquam dapibus finibus mauris in molestie.</p>
  </section>

  <section class="review abs" style="left:356px">
    <h4><span class="stars">
      <svg viewBox="0 0 12 12"><polygon points="6,0.5 7.6,4.3 11.6,4.5 8.5,7 9.5,11 6,8.8 2.5,11 3.5,7 0.4,4.5 4.4,4.3" fill="#d4458c"/></svg>
      <svg viewBox="0 0 12 12"><polygon points="6,0.5 7.6,4.3 11.6,4.5 8.5,7 9.5,11 6,8.8 2.5,11 3.5,7 0.4,4.5 4.4,4.3" fill="#d4458c"/></svg>
      <svg viewBox="0 0 12 12"><polygon points="6,0.5 7.6,4.3 11.6,4.5 8.5,7 9.5,11 6,8.8 2.5,11 3.5,7 0.4,4.5 4.4,4.3" fill="#d4458c"/></svg>
      <svg viewBox="0 0 12 12"><polygon points="6,0.5 7.6,4.3 11.6,4.5 8.5,7 9.5,11 6,8.8 2.5,11 3.5,7 0.4,4.5 4.4,4.3" fill="#d4458c"/></svg>
      <svg viewBox="0 0 12 12"><polygon points="6,0.5 7.6,4.3 11.6,4.5 8.5,7 9.5,11 6,8.8 2.5,11 3.5,7 0.4,4.5 4.4,4.3" fill="#e9a9c8"/></svg>
    </span>&nbsp;AENEAN <span class="date">&nbsp;| 10 MARCH 2017</span></h4>
    <p>Vivamus ultricies mauris leo, a egestas odio aliquet id. Duis fringilla justo nec placerat rutrum. Proin magna magna, condimentum tempus elit ut, venenatis lobortis orci.</p>
  </section>

  <footer class="site-footer abs">
    <dl class="contact abs">
      <dt>ADDRESS</dt><dd>ORCHARD 42 STR.</dd>
      <dt>ZIPCODE</dt><dd>10218</dd>
      <dt>STADE</dt><dd>NEW YORK</dd>
      <dt>PHONE</dt><dd>+30-2105550142</dd>
    </dl>
    <div class="foot-brand abs"><div class="mark" role="img" aria-label="Grinvault mascot emblem"></div><span>GRINVAULT</span></div>
    <div class="foot-social abs">
      <a href="#">picshelf</a><a href="#">chirpline</a><a href="#">friendwall</a><a href="#">pinvale</a>
    </div>
    <div class="copyright abs">COPY RIGHT © 2017 GRINVAULT</div>
  </footer>

</main>
</body>
</html>
```